New Product Catalog for 9 Products

We need a new product brochure-catalog for our 9 products. Please group them in 3 categories, supplements, skin care & tea-powder. Will need prices next to the products also. Attached is our current brochure, which is too busy looking. I'll upload more images also. You can check our website to get a feel of who we are. www.tqharbor.com

Target Market(s)

Half of our market speaks Spanish, will have it translated from English next.

Industry/Entity Type

Health And Wellness

Colors

Designer to choose colors to be used in the design.

Requirements
Must have
• Use the moringa theme we have on our website also. Please group the supplements, skin care, & tea-powder, so have 3 sections.
Nice to have
• Keep the colors the same as our website please

```html
<!DOCTYPE html>
<html lang="en">
<head>
<meta charset="utf-8">
<title>TQ Harbor Product Catalog</title>
<link href="https://fonts.googleapis.com/css2?family=Raleway:wght@300&family=Arimo:wght@400;700&display=swap" rel="stylesheet">
<style>
  :root {
    --green: #3aa935;
    --orange: #f39c12;
    --lime: #c5d12c;
    --ink: #1e1e1e;
    --paper: #ffffff;
    --fold: #d9d9d9;
  }
  * { margin: 0; padding: 0; box-sizing: border-box; }
  html, body { width: 1200px; height: 736px; overflow: hidden; }
  body {
    position: relative;
    font-family: "Arimo", Arial, sans-serif;
    color: var(--ink);
    background:
      linear-gradient(to right,
        var(--paper) 0, var(--paper) 548px,
        var(--fold) 585px, var(--paper) 625px,
        var(--paper) 668px, var(--fold) 700px, var(--paper) 728px,
        var(--paper) 100%);
  }

  .section-title {
    position: absolute;
    font-family: "Raleway", sans-serif;
    font-weight: 300;
    font-size: 55px;
    line-height: 1;
    letter-spacing: -1px;
  }
  .frame { position: absolute; border-style: solid; }
  .frame-rule { position: absolute; height: 2px; }

  .supplements-title { left: 40px; top: 12px; color: var(--green); }
  .supplements-frame { left: 27px; top: 73px; width: 773px; height: 344px; border-color: var(--green); border-width: 0 2px 2px 2px; }
  .supplements-rule { left: 395px; top: 34px; width: 405px; background: var(--green); }
  .supplements-side { position: absolute; left: 798px; top: 34px; width: 2px; height: 40px; background: var(--green); }

  .skincare-title { left: 40px; top: 420px; color: var(--orange); }
  .skincare-frame { left: 27px; top: 469px; width: 773px; height: 249px; border-color: var(--orange); border-width: 0 2px 2px 2px; }
  .skincare-rule { left: 374px; top: 447px; width: 426px; background: var(--orange); }
  .skincare-side { position: absolute; left: 798px; top: 447px; width: 2px; height: 23px; background: var(--orange); }

  .tea-title { left: 817px; top: 16px; color: var(--lime); }
  .tea-frame { left: 807px; top: 66px; width: 370px; height: 652px; border-color: var(--lime); border-width: 0 2px 2px 2px; }
  .tea-rule { left: 1110px; top: 34px; width: 67px; background: var(--lime); }
  .tea-side { position: absolute; left: 1175px; top: 34px; width: 2px; height: 33px; background: var(--lime); }

  .photo { position: absolute; border-radius: 6px; }
  .photo-bottle { background: linear-gradient(to bottom, #f4f4f4 0, #ffffff 30%, #7bc043 60%, #ffffff 85%, #e9e9e9 100%); }
  .photo-pouch { background: linear-gradient(160deg, #e2d9e7 0, #c9b7d3 55%, #7e4d2a 100%); }
  .photo-lotion { background: linear-gradient(to bottom, #e6e6e6 0, #e6e6e6 22%, #f2c6dc 30%, #e7a7c8 80%, #9d6fa0 100%); border-radius: 10px; }
  .photo-oil { background: linear-gradient(to bottom, #3a2a1a 0, #3a2a1a 18%, #b5651d 28%, #d98b2c 60%, #8fb43a 85%, #b5651d 100%); }
  .photo-balm { background: linear-gradient(to bottom, #f3f3e4 0, #e8ecc0 50%, #c9c9c9 100%); border-radius: 14px; }
  .photo-plant { background: radial-gradient(ellipse at 50% 50%, #eee877 0, #a8c94a 35%, rgba(168,201,74,0.35) 58%, rgba(255,255,255,0) 72%); }

  .product { position: absolute; display: flex; flex-direction: column; align-items: flex-start; }
  .product-name { color: var(--orange); font-size: 12.5px; line-height: 14px; }
  .product-line { font-size: 11px; text-transform: uppercase; line-height: 14px; margin-top: 3px; }
  .tagline { color: var(--orange); font-weight: 700; font-size: 13px; line-height: 17px; margin-top: 4px; }
  .tagline-large { font-size: 14px; line-height: 19px; }
  .description { font-size: 6.8px; line-height: 9.6px; margin-top: 4px; text-align: justify; width: 100%; }
  .description-left { text-align: left; }
  .price {
    margin-top: auto;
    width: 66px; height: 28px;
    line-height: 28px;
    text-align: center;
    background: var(--green);
    color: var(--paper);
    font-size: 14px;
    flex-shrink: 0;
  }
  .footnote { position: absolute; left: 835px; top: 673px; width: 172px; font-size: 6.4px; line-height: 1.4; }
</style>
</head>
<body>

  <!-- supplements -->
  <div class="frame supplements-frame"></div>
  <div class="frame-rule supplements-rule"></div>
  <div class="supplements-side"></div>
  <h2 class="section-title supplements-title">supplements</h2>

  <div class="photo photo-bottle" role="img" aria-label="TQ7 supplement bottle" style="left:44px;top:90px;width:80px;height:134px;"></div>
  <div class="product" style="left:139px;top:97px;width:272px;height:137px;">
    <p class="product-name">TQ7</p>
    <p class="product-line">7 Superfoods for super health</p>
    <p class="tagline">One isn't enough, so we give you 7</p>
    <p class="description">TQ7 is our superfood powered super supplement. Each of the 7 minimally processed, whole food ingredients of TQ7 can be considered superfoods by themselves, but together these fruits and vegetables are even stronger. We designed TQ7 to give our bodies a little extra support, filling in the nutritional holes in our diets. Besides the obvious antioxidants and nutrition that TQ7 provides, its also a solid source of fiber.*</p>
    <span class="price">34.95</span>
  </div>

  <div class="photo photo-bottle" role="img" aria-label="TQ7 supplement bottle" style="left:442px;top:90px;width:66px;height:134px;"></div>
  <div class="product" style="left:527px;top:97px;width:262px;height:137px;">
    <p class="product-name">TQ7</p>
    <p class="product-line">7 Superfoods for super health</p>
    <p class="tagline">One isn't enough, so we give you 7</p>
    <p class="description">TQ7 is our superfood powered super supplement. Each of the 7 minimally processed, whole food ingredients of TQ7 can be considered superfoods by themselves, but together these fruits and vegetables are even stronger. We designed TQ7 to give our bodies a little extra support, filling in the nutritional holes in our diets. Besides the obvious antioxidants and nutrition that TQ7 provides, its also a solid source of fiber.*</p>
    <span class="price">34.95</span>
  </div>

  <div class="photo photo-bottle" role="img" aria-label="TQ7 supplement bottle" style="left:44px;top:258px;width:80px;height:134px;"></div>
  <div class="product" style="left:139px;top:262px;width:272px;height:138px;">
    <p class="product-name">TQ7</p>
    <p class="product-line">7 Superfoods for super health</p>
    <p class="tagline">One isn't enough, so we give you 7</p>
    <p class="description">TQ7 is our superfood powered super supplement. Each of the 7 minimally processed, whole food ingredients of TQ7 can be considered superfoods by themselves, but together these fruits and vegetables are even stronger. We designed TQ7 to give our bodies a little extra support, filling in the nutritional holes in our diets. Besides the obvious antioxidants and nutrition that TQ7 provides, its also a solid source of fiber.*</p>
    <span class="price">34.95</span>
  </div>

  <div class="photo photo-bottle" role="img" aria-label="TQ7 supplement bottle" style="left:442px;top:258px;width:66px;height:134px;"></div>
  <div class="product" style="left:524px;top:262px;width:265px;height:138px;">
    <p class="product-name">TQ7</p>
    <p class="product-line">7 Superfoods for super health</p>
    <p class="tagline">One isn't enough, so we give you 7</p>
    <p class="description">TQ7 is our superfood powered super supplement. Each of the 7 minimally processed, whole food ingredients of TQ7 can be considered superfoods by themselves, but together these fruits and vegetables are even stronger. We designed TQ7 to give our bodies a little extra support, filling in the nutritional holes in our diets. Besides the obvious antioxidants and nutrition that TQ7 provides, its also a solid source of fiber.*</p>
    <span class="price">34.95</span>
  </div>

  <!-- skin care -->
  <div class="frame skincare-frame"></div>
  <div class="frame-rule skincare-rule"></div>
  <div class="skincare-side"></div>
  <h2 class="section-title skincare-title">skin care</h2>

  <div class="photo photo-oil" role="img" aria-label="Organic moringa oil dropper bottle" style="left:111px;top:477px;width:56px;height:225px;"></div>
  <div class="product" style="left:222px;top:493px;width:202px;height:219px;">
    <p class="product-line">7 Superfoods<br>for super health</p>
    <p class="tagline tagline-large">100% Pure; no<br>additives, no carrier<br>oils, no fragrance</p>
    <p class="description description-left" style="margin-top:12px;">Moringa Oil has a multitude of health benefits. It is a great moisturizer and healing agent for dry, damaged skin and is also great when used on minor cuts and abrasions. Moringa oil is rich in antioxidants and is known to be antiseptic. Because of its antioxidant and fatty acid profile, Moringa oil has been used in beauty and anti-aging applications.<br>Use our 100% Organic Moringa Oil on you hair, skin and nails or even try it in your next bath.</p>
    <span class="price">34.95</span>
  </div>

  <div class="photo photo-balm" role="img" aria-label="Moringa body balm jar with open lid" style="left:442px;top:516px;width:147px;height:107px;"></div>
  <div class="product" style="left:600px;top:514px;width:190px;height:198px;">
    <p class="product-name">TQ7</p>
    <p class="product-line">7 Superfoods<br>for super health</p>
    <p class="tagline">One isn't enough,<br>so we give you 7</p>
    <p class="description description-left">TQ7 is our superfood powered super supplement. Each of the 7 minimally processed, whole food ingredients of TQ7 can be considered superfoods by themselves, but together these fruits and vegetables are even stronger. We designed TQ7 to give our bodies a little extra support, filling in the nutritional holes in our diets. Besides the obvious antioxidants and nutrition that TQ7 provides, its also a solid source of fiber.*</p>
    <span class="price">34.95</span>
  </div>

  <!-- tea-powder -->
  <div class="frame tea-frame"></div>
  <div class="frame-rule tea-rule"></div>
  <div class="tea-side"></div>
  <h2 class="section-title tea-title">tea-powder</h2>

  <div class="photo photo-pouch" role="img" aria-label="Moringa tea pouch" style="left:818px;top:101px;width:103px;height:140px;"></div>
  <div class="product" style="left:942px;top:97px;width:205px;height:185px;">
    <p class="product-name">TQ7</p>
    <p class="product-line">7 Superfoods for super health</p>
    <p class="tagline">One isn't enough,<br>so we give you 7</p>
    <p class="description description-left">TQ7 is our superfood powered super supplement. Each of the 7 minimally processed, whole food ingredients of TQ7 can be considered superfoods by themselves, but together these fruits and vegetables are even stronger. We designed TQ7 to give our bodies a little extra support, filling in the nutritional holes in our diets. Besides the obvious antioxidants and nutrition that TQ7 provides, its also a solid source of fiber.*</p>
    <span class="price">34.95</span>
  </div>

  <div class="photo photo-lotion" role="img" aria-label="Moringa citrus lotion pump bottle" style="left:844px;top:334px;width:83px;height:227px;"></div>
  <div class="product" style="left:953px;top:333px;width:205px;height:211px;">
    <p class="product-name">MORINGA</p>
    <p class="product-line">Small capsule, big nutrition</p>
    <p class="tagline" style="margin-top:18px;">its about time you<br>get caught up!</p>
    <p class="description description-left" style="margin-top:8px;">TQ7 is our superfood powered super supplement. Each of the 7 minimally processed, whole food ingredients of TQ7 can be considered superfoods by themselves, but together these fruits and vegetables are even stronger. We designed TQ7 to give our bodies a little extra support, filling in the nutritional holes in our diets. Besides the obvious antioxidants and nutrition that TQ7 provides, its also a solid source of fiber.*</p>
    <span class="price">34.95</span>
  </div>

  <div class="photo photo-plant" role="img" aria-label="Moringa leaves and flowers sprig" style="left:960px;top:525px;width:200px;height:175px;"></div>

  <p class="footnote">* These statements have not been evaluated by the FDA. These products are not intended to diagnose, treat, cure, or prevent any disease.</p>

</body>
</html>
```